Quorvel Heating Post Card

Take text from existing file and put into a vibrant post card (also needs back) to send to potential customer in two formats, via email and mail services so want the piece to fit both media types.
Please include bleed for printing.

Include logo, telephone number and web address.

Target Market(s)

Mechanical Contractors

Font styles to use
Sans Serif

Colors
fbed22
0456a4
3176b5
ec1f27

Requirements
Must have
• Text and pictures uploaded with exception of bundled picture on the text file.
• Must be vibrant but not too over the top.

```html
<!DOCTYPE html>
<html lang="en">
<head>
<meta charset="utf-8">
<title>Quorvel Heating Post Card</title>
<link rel="stylesheet" href="https://fonts.googleapis.com/css2?family=Open+Sans:wght@400;600;700&family=Oswald:wght@500;600;700&display=swap">
<style>
  :root {
    --yellow: #fbed22;
    --blue: #0456a4;
    --blue-light: #3176b5;
    --red: #ec1f27;
    --ink: #1d1d1d;
    --paper: #ffffff;
    --panel: #f1f1f1;
    --stage: #e6e6e6;
    --line: #8a8a8a;
  }
  * { box-sizing: border-box; margin: 0; padding: 0; }
  html, body { width: 852px; height: 1200px; overflow: hidden; }
  body { background: var(--stage); font-family: "Open Sans", Arial, sans-serif; color: var(--ink); position: relative; }

  .card { position: absolute; left: 96px; width: 660px; height: 500px; background: var(--paper); overflow: hidden; box-shadow: 0 4px 14px rgba(0,0,0,.18); }
  .card--front { top: 60px; background: linear-gradient(180deg, #fff 0%, #f2f2f2 75%); }
  .card--back { top: 630px; }

  /* Front */
  .services-tab { position: absolute; left: 0; top: 23px; width: 281px; height: 45px; background: linear-gradient(180deg, var(--blue-light), var(--blue)); border-radius: 0 10px 10px 0; color: #fff; font-weight: 700; font-size: 23px; padding: 9px 0 0 34px; letter-spacing: .3px; }
  .service-list { position: absolute; left: 16px; top: 94px; list-style: none; }
  .service { position: relative; padding-left: 27px; margin-bottom: 10px; }
  .service::before { content: ""; position: absolute; left: 0; top: 4px; width: 16px; height: 16px; border-radius: 50%; background: var(--red); }
  .service::after { content: ""; position: absolute; left: 4px; top: 9px; width: 5px; height: 5px; border-right: 2px solid #fff; border-top: 2px solid #fff; transform: rotate(45deg); }
  .service__name { color: var(--red); font-weight: 600; font-size: 16px; text-transform: uppercase; }
  .service__range { color: var(--ink); font-size: 12.5px; font-weight: 400; text-transform: none; }
  .service__detail { display: block; font-size: 12px; margin-top: 1px; }

  .equipment-photo { position: absolute; left: 376px; top: 20px; width: 274px; height: 372px; background: linear-gradient(160deg, #cfd3d8 0%, #9aa3ad 45%, #e4c34a 80%, #3a3a3a 100%); opacity: .85; border-radius: 6px; }

  .response-badge { position: absolute; left: 344px; top: 282px; width: 96px; height: 96px; border-radius: 50%; background: var(--red); border: 4px solid #fff; box-shadow: 0 2px 6px rgba(0,0,0,.35); text-align: center; font-family: "Oswald", Arial, sans-serif; color: #fff; }
  .response-badge__top { display: block; font-size: 15px; margin-top: 6px; line-height: 1; color: var(--ink); }
  .response-badge__big { display: block; font-size: 38px; font-weight: 700; line-height: 1; }
  .response-badge__bottom { display: block; font-size: 14px; line-height: 1; color: var(--ink); }

  .front-footer { position: absolute; left: 0; top: 350px; width: 660px; height: 150px; }
  .quote-tab { position: absolute; right: 10px; top: 395px; width: 222px; height: 30px; background: linear-gradient(180deg, var(--blue-light), var(--blue)); border-radius: 8px 0 0 8px; color: #fff; font-family: "Oswald", Arial, sans-serif; font-weight: 500; font-size: 16px; text-align: center; line-height: 30px; }
  .front-web { position: absolute; right: 14px; top: 434px; color: #fff; font-size: 13px; font-weight: 600; }
  .front-call { position: absolute; right: 14px; top: 458px; font-family: "Oswald", Arial, sans-serif; font-weight: 600; font-size: 24px; color: #fff; }
  .front-call span, .back-call span { color: var(--yellow); }

  .brand { position: absolute; display: flex; align-items: center; gap: 8px; }
  .brand__dot { width: 40px; height: 40px; border-radius: 50%; background: var(--blue); }
  .brand__name { font-family: "Open Sans", Arial, sans-serif; font-weight: 700; font-size: 19px; color: var(--red); line-height: 1.05; }
  .card--front .brand { left: 22px; top: 430px; }

  /* Back */
  .back-panel { position: absolute; left: 0; top: 0; width: 400px; height: 500px; }
  .card--back .brand { left: 58px; top: 36px; }
  .card--back .brand__dot { width: 48px; height: 48px; }
  .card--back .brand__name { font-size: 22px; }
  .rapid-band { position: absolute; left: 0; top: 110px; width: 356px; height: 46px; color: #fff; font-weight: 700; font-size: 17px; text-align: center; line-height: 46px; padding-right: 40px; }
  .fleet-photo { position: absolute; left: 0; top: 156px; width: 362px; height: 256px; background: linear-gradient(170deg, #d6d8db 0%, #a8adb3 55%, #8b8f94 100%); }
  .back-call { position: absolute; left: 38px; top: 430px; font-family: "Oswald", Arial, sans-serif; font-weight: 600; font-size: 20px; color: #fff; }
  .back-web { position: absolute; left: 38px; top: 460px; color: #fff; font-size: 14px; font-weight: 600; }

  .stamp-box { position: absolute; left: 526px; top: 19px; width: 99px; height: 63px; border: 1px solid var(--line); }
  .address-line { position: absolute; left: 409px; width: 223px; height: 1px; background: var(--line); }
</style>
</head>
<body>

<section class="card card--front" aria-label="Post card front">
  <div class="services-tab">OUR SERVICES</div>
  <ul class="service-list">
    <li class="service"><span class="service__name">Electric Heaters <span class="service__range">(10kW - 150kW)</span></span><span class="service__detail">240 Volt Single Phase to 480 Volt Three Phase</span></li>
    <li class="service"><span class="service__name">Direct Fired Heaters <span class="service__range">(70,000 - 4,000,000 BTU)</span></span><span class="service__detail">Natural Gas, Propane or Fuel Oil</span></li>
    <li class="service"><span class="service__name">Indirect Fired Heaters <span class="service__range">(100,000 - 1,500,000 BTU</span></span><span class="service__detail">Natural Gas, Propane or Fuel Oil</span></li>
    <li class="service"><span class="service__name">Propane Patio Heaters <span class="service__range">(0 - 40,000 BTU)</span></span></li>
    <li class="service"><span class="service__name">Heat Exchangers <span class="service__range">(100 - 3000 sq ft)</span></span></li>
    <li class="service"><span class="service__name">Boilers <span class="service__range">(15HP - 200 HP)</span></span></li>
  </ul>

  <div class="equipment-photo" role="img" aria-label="Portable heaters: electric heater, direct fired heater, patio heater and fan heater"></div>

  <svg class="front-footer" viewBox="0 0 660 150" aria-hidden="true">
    <rect x="0" y="55" width="660" height="95" fill="var(--red)"/>
    <path d="M0 22 Q150 -10 265 80 L300 150 L0 150 Z" fill="var(--blue)"/>
    <path d="M0 32 Q140 4 250 84 L282 150 L0 150 Z" fill="#fff"/>
  </svg>

  <div class="response-badge">
    <span class="response-badge__top">RAPID</span>
    <span class="response-badge__big">24/7</span>
    <span class="response-badge__bottom">RESPONSE</span>
  </div>

  <div class="brand"><span class="brand__dot"></span><span class="brand__name">Quorvel<br>Heating</span></div>

  <div class="quote-tab">CALL FOR YOUR QUOTE TODAY</div>
  <div class="front-web">www.quorvelheating.com</div>
  <div class="front-call">CALL US TODAY: <span>888-555-0147</span></div>
</section>

<section class="card card--back" aria-label="Post card back">
  <svg class="back-panel" viewBox="0 0 400 500" aria-hidden="true">
    <defs>
      <linearGradient id="panelFade" x1="0" y1="0" x2="0" y2="1">
        <stop offset="0" stop-color="#fff"/>
        <stop offset="1" stop-color="#e2e2e2"/>
      </linearGradient>
      <linearGradient id="blueBand" x1="0" y1="0" x2="0" y2="1">
        <stop offset="0" stop-color="var(--blue-light)"/>
        <stop offset="1" stop-color="var(--blue)"/>
      </linearGradient>
    </defs>
    <path d="M0 0 H352 Q410 250 362 500 H0 Z" fill="url(#panelFade)"/>
    <path d="M0 110 H374 Q377 133 378 156 H0 Z" fill="var(--red)"/>
    <path d="M0 413 H382 Q378 458 370 500 H0 Z" fill="url(#blueBand)"/>
    <path d="M352 0 Q410 250 362 500" fill="none" stroke="#cfcfcf" stroke-width="3"/>
  </svg>

  <div class="brand"><span class="brand__dot"></span><span class="brand__name">Quorvel<br>Heating</span></div>
  <div class="rapid-band">24/7 RAPID RESPONSE</div>
  <div class="fleet-photo" role="img" aria-label="Group of portable heaters on a grey floor"></div>
  <div class="back-call">CALL US TODAY: <span>888-555-0147</span></div>
  <div class="back-web">www.quorvelheating.com</div>

  <div class="stamp-box"></div>
  <div class="address-line" style="top:194px"></div>
  <div class="address-line" style="top:234px"></div>
  <div class="address-line" style="top:273px"></div>
  <div class="address-line" style="top:311px"></div>
</section>

</body>
</html>
```